Dutch craft distillery needs labels designed for Gin bottle

We are a small craft distillery based in The Netherlands. We are currently producing only GIN. While we do have a logo for our distillery, we are still in search of a winning design for our Gin bottle. We are looking for something modern yet classy. Let your creativity run wild. Play around with colours, think out of the box….The winning designer will be challenged to create the coolest labels for the different flavours of Gin we will be producing in the near future. The label will maintain the same design elements throughout the design, but will also be able to differentiate each variety clearly. So for e.g. A flowery VosKamp Gin can have a pink label with a different description and a spicy VosKamp gin can have another colour with another description and so on. If the design really appeals to us, we might also invite the designer to do our website for us!

In a nutshell: It is a 500 ml bottle, (Please check the attachment so you get an idea as to what kind of bottle to imagine while making the labels). The bottle is going to have a light coloured wooden lid/cork to it. As of now we have a transparent seal to complete the sealing process once the bottling is done. The idea is that we will have two labels. One in the front and one behind. The size of the labels are as follows:

Front label: 102 x 76 mm the front label. (TO BE USED HORIZONTALLY). The details that we need on the front label are in a separate attachment.

Back label: The size for the label at the back of the bottle is: 76 x 51 mm (TO BE USED VERTICALLY) The information that needs to come on the label behind is also in the same document which is attached separately. The label behind will also have batch no. & date (Please refer to attachment to understand what I mean by batch no. date, distiller’s signature etc.) I have attached a picture of an already existing brand which has its batch number and distillers signature etc on it….so you can understand what I exactly mean by that. Please do not copy their design, this is purely to give you an idea as to what I mean by batch number and so on. The address of the distillery can be put horizontally, vertically, on the side along one border, or however you find appropriate. This is the address:
Berkenhoutlaan 41,
7311 KD, Hengelo.
The Netherlands.
www.voskamp.nl

Logo’s no drinking when pregnant, No driving and drinking, No drinking under the age of 18 need to be present on the label behind. Alternately, we can also have www.calm-sipping.com instead of the under 18 no alcohol sign, most alcohol bottles these days have it. Please let me know what else you would need from me for this. So be creative and do your best!

Thanks and regards, Marisol Venkataraghavan.

Target Market(s)

Largely males and females between 25-55 , the audience could even be slightly older.

Colors

Designer to choose colors to be used in the design.

Requirements
Must have
• 1) The labels need to be modern, yet classy, elite..
• 2) We need to specify the fact that we are a craft distillery and the gin is HANDMADE, using only the highest quality ingredients.
• 3) We at VosKamp live, breathe, dream, talk about our dream which is our distillery and its product. The label needs to bring home this point and should clearly specify and mention that it is produced and bottled in The Netherlands. Or handmade and bottled with love and passion in The Netherlands or something to that effect if it matches with the rest of the design.
• 4) The colours you chose must match in some way or the other with the colours used for the logo design.
Nice to have
• Would be nice to have colours and look bold, although not completely necessary.
Should not have
• What I definitely do not want is something too whacky like a skull or some kind of vague work of art. For the rest, I leave it upto you….!

```html
<!DOCTYPE html>
<html lang="en">
<head>
<meta charset="utf-8">
<title>VosKamp Gin – Front Label</title>
<link rel="stylesheet" href="https://fonts.googleapis.com/css2?family=Rye&family=Old+Standard+TT:wght@400;700&family=IM+Fell+English+SC&display=swap">
<style>
  :root {
    --backdrop: #9aa6b8;
    --label-black: #141414;
    --label-stripe: #1f1f1f;
    --copper: #c07a3e;
    --copper-light: #e2a867;
    --cream: #efe2c8;
    --silver: #e9e9e9;
    --ribbon: #f2f0ea;
    --ink: #111111;
  }
  html, body {
    margin: 0;
    padding: 0;
    overflow: hidden;
  }
  body {
    width: 794px;
    height: 1200px;
    background: var(--backdrop);
    position: relative;
    font-family: "Old Standard TT", serif;
  }
  .front-label {
    position: absolute;
    left: 45px;
    top: 344px;
    width: 704px;
    height: 512px;
    background:
      repeating-linear-gradient(0deg, var(--label-black) 0 3px, var(--label-stripe) 3px 5px);
    box-sizing: border-box;
    border: 4px solid var(--copper);
  }
  .frame-outer, .frame-inner {
    position: absolute;
    border: 2px solid var(--copper);
    pointer-events: none;
  }
  .frame-outer { inset: 10px; }
  .frame-inner { inset: 17px; border-width: 1px; border-color: var(--copper-light); }

  .distillery-name {
    position: absolute;
    top: 50px;
    left: 0;
    width: 100%;
    text-align: center;
    font-family: "Rye", serif;
    font-size: 15px;
    letter-spacing: 1px;
    color: var(--copper-light);
  }
  .brand-title {
    position: absolute;
    top: 110px;
    left: 0;
    width: 100%;
    text-align: center;
    font-family: "Rye", serif;
    font-size: 92px;
    line-height: 1;
    letter-spacing: 4px;
    background: linear-gradient(90deg, var(--copper) 0%, var(--cream) 50%, var(--copper) 100%);
    -webkit-background-clip: text;
    background-clip: text;
    color: transparent;
  }
  .product-type {
    position: absolute;
    top: 222px;
    left: 0;
    width: 100%;
    text-align: center;
    font-family: "Old Standard TT", serif;
    font-weight: 700;
    font-size: 70px;
    line-height: 1;
    color: var(--silver);
  }
  .style-ribbon {
    position: absolute;
    left: 216px;
    top: 312px;
    width: 282px;
    height: 42px;
  }
  .style-ribbon-text {
    position: absolute;
    left: 216px;
    top: 320px;
    width: 282px;
    text-align: center;
    font-family: "IM Fell English SC", serif;
    font-size: 17px;
    color: var(--ink);
  }
  .producer-line {
    position: absolute;
    top: 360px;
    left: 0;
    width: 100%;
    text-align: center;
    font-size: 7px;
    letter-spacing: 0.5px;
    color: var(--silver);
  }
  .claims {
    position: absolute;
    top: 396px;
    left: 0;
    width: 100%;
    text-align: center;
    font-size: 13px;
    line-height: 18px;
    color: var(--silver);
  }
  .volume {
    position: absolute;
    top: 446px;
    left: 0;
    width: 100%;
    text-align: center;
    font-size: 13px;
    color: var(--silver);
  }
  .origin {
    position: absolute;
    top: 467px;
    left: 0;
    width: 100%;
    text-align: center;
    font-size: 6px;
    letter-spacing: 0.5px;
    color: var(--silver);
  }
  .craft-seal {
    position: absolute;
    left: 58px;
    top: 306px;
    width: 120px;
    height: 120px;
  }
  .windmill-artwork {
    position: absolute;
    left: 493px;
    top: 268px;
    width: 176px;
    height: 192px;
    background: linear-gradient(180deg, #d9c7a8 0%, #b8874f 100%);
    opacity: 0.85;
  }
</style>
</head>
<body>
  <section class="front-label">
    <div class="frame-outer"></div>
    <div class="frame-inner"></div>

    <div class="distillery-name">VOSKAMP DISTILLERY</div>
    <h1 class="brand-title" style="margin:0;">VOSKAMP</h1>
    <div class="product-type">GIN</div>

    <svg class="style-ribbon" viewBox="0 0 282 42" aria-hidden="true">
      <path d="M0 8 L18 8 L12 18 L18 30 L0 30 Z" fill="var(--ribbon)"/>
      <path d="M282 8 L264 8 L270 18 L264 30 L282 30 Z" fill="var(--ribbon)"/>
      <rect x="14" y="4" width="254" height="30" fill="var(--ribbon)" stroke="var(--ink)" stroke-width="1"/>
    </svg>
    <div class="style-ribbon-text">PREMIUM LONDON DRY GIN</div>

    <div class="producer-line">DISTILLED AND BOTTLED BY VOSKAMP DISTILLERY</div>
    <div class="claims">100% NATURAL BOTANICALS<br>NO ARTIFICIAL FLAVOURING</div>
    <div class="volume">50 CL | 43% VOL</div>
    <div class="origin">PRODUCT OF THE NETHERLANDS</div>

    <svg class="craft-seal" viewBox="0 0 120 120" aria-hidden="true">
      <circle cx="60" cy="60" r="56" fill="none" stroke="var(--copper)" stroke-width="3"/>
    </svg>

    <div class="windmill-artwork" role="img" aria-label="Copper illustration of a Dutch windmill with tulips"></div>
  </section>
</body>
</html>
```